" ATENDEMOS CLIENTES DE BALCÃO PARA VENDA DE PEÇAS E PNEUS DA LINHA LEVE + CAMIONETES NACIONAIS E IMPORTADOS. CONTAMOS COM UM CENTRO AUTOMOTIVO DE GRANDE PORTE PARA EXECUTAR SERVIÇOS MECÂNICOS DE REVISÃO E MANUTENÇÃO CORRETIVA E PREVENTIVA ( ALINHAMENTO, BALANCEAMENTO, MONTAGEM DE PNEUS, SUSPENSÃO, FREIOS, CAMBIO MANUAL E AUTOMATIZADO, INJEÇÃO ELETRÔNICA, REPARO DE MOTOR E CABEÇOTES, SISTEMA DE DIREÇÃO ). "

```html
<!DOCTYPE html>
<html lang="en">
<head>
<meta charset="utf-8">
<title>Torque Auto Letterhead</title>
<link href="https://fonts.googleapis.com/css2?family=Montserrat:wght@800&family=Open+Sans:wght@400;600&display=swap" rel="stylesheet">
<style>
  :root {
    --backdrop: #1b222a;
    --paper: #ffffff;
    --ink: #2b2f36;
    --muted: #6b717a;
    --brand-red: #d7262c;
    --brand-navy: #1c2533;
    --signature-tone: #c9ccd1;
  }
  html, body {
    margin: 0;
    width: 1200px;
    height: 1200px;
    overflow: hidden;
    background: var(--backdrop);
  }
  .letterhead {
    position: absolute;
    left: 190px;
    top: 20px;
    width: 820px;
    height: 1160px;
    background: var(--paper);
    font-family: "Open Sans", sans-serif;
    color: var(--ink);
    overflow: hidden;
  }
  .brand {
    position: absolute;
    top: 70px;
    right: 80px;
    display: flex;
    align-items: center;
    gap: 10px;
  }
  .brand-dot {
    width: 14px;
    height: 14px;
    border-radius: 50%;
    background: var(--brand-red);
  }
  .brand-name {
    font-family: "Montserrat", sans-serif;
    font-weight: 800;
    font-size: 30px;
    letter-spacing: 1px;
    color: var(--brand-red);
  }
  .recipient {
    position: absolute;
    top: 70px;
    left: 80px;
    font-size: 14px;
    line-height: 1.5;
    font-weight: 600;
  }
  .recipient p { margin: 0; }
  .letter-date {
    position: absolute;
    top: 270px;
    right: 80px;
    font-size: 13px;
    color: var(--muted);
    text-align: right;
  }
  .letter-body {
    position: absolute;
    top: 320px;
    left: 80px;
    right: 80px;
    font-size: 13.5px;
    line-height: 1.75;
    color: var(--muted);
  }
  .letter-body p { margin: 0 0 18px; }
  .sign-off {
    position: absolute;
    top: 650px;
    left: 80px;
    font-size: 13.5px;
    color: var(--muted);
  }
  .signature {
    margin-top: 14px;
    width: 150px;
    height: 70px;
    background: var(--signature-tone);
    border-radius: 6px;
  }
  .contact-bar {
    position: absolute;
    left: 80px;
    right: 80px;
    bottom: 92px;
    display: flex;
    justify-content: space-between;
    font-size: 12.5px;
    color: var(--muted);
  }
  .contact-item {
    display: flex;
    align-items: center;
    gap: 8px;
  }
  .contact-item svg { width: 16px; height: 16px; fill: var(--brand-red); }
  .edge-bands {
    position: absolute;
    left: 0;
    bottom: 0;
    width: 820px;
    height: 60px;
  }
</style>
</head>
<body>
<main class="letterhead">
  <header class="brand">
    <span class="brand-dot"></span>
    <span class="brand-name">TORQUE AUTO</span>
  </header>

  <section class="recipient">
    <p>To,</p>
    <p>Mr. Daniel Ferraz</p>
    <p>Purchasing Manager</p>
    <p>Ferraz Transportes Ltda</p>
    <p>Av. Central, 1200</p>
    <p>Curitiba, Paraná 80000</p>
  </section>

  <div class="letter-date">Date: 10 May 2024</div>

  <section class="letter-body">
    <p>Dear Mr. Ferraz, thank you for your interest in our counter sales of parts and tyres for light vehicles and pickups, both national and imported. We are pleased to present our full service centre to your fleet team.</p>
    <p>Our workshop performs preventive and corrective maintenance, including alignment, balancing, tyre fitting, suspension, brakes, manual and automated gearboxes, electronic injection, engine and cylinder head repair and steering systems, all handled by trained technicians.</p>
    <p>Please find attached our price table for the coming quarter. We would be glad to schedule a visit and discuss a maintenance plan that suits your vehicles and routine.</p>
  </section>

  <section class="sign-off">
    <div>Sincerely,</div>
    <div class="signature" role="img" aria-label="Handwritten signature of the sender"></div>
  </section>

  <footer class="contact-bar">
    <span class="contact-item">
      <svg viewBox="0 0 24 24"><path d="M12 2a7 7 0 0 0-7 7c0 5 7 13 7 13s7-8 7-13a7 7 0 0 0-7-7zm0 9.5A2.5 2.5 0 1 1 12 6.5a2.5 2.5 0 0 1 0 5z"/></svg>
      Rua das Oficinas, 450 Centro
    </span>
    <span class="contact-item">
      <svg viewBox="0 0 24 24"><path d="M3 5h18v14H3z M3 5l9 7 9-7" fill="none" stroke="#d7262c" stroke-width="2"/></svg>
      contato@torqueauto.com.br
    </span>
    <span class="contact-item">
      <svg viewBox="0 0 24 24"><path d="M6.6 10.8a15 15 0 0 0 6.6 6.6l2.2-2.2a1 1 0 0 1 1-.25 11.4 11.4 0 0 0 3.6.57 1 1 0 0 1 1 1V20a1 1 0 0 1-1 1A17 17 0 0 1 3 4a1 1 0 0 1 1-1h3.5a1 1 0 0 1 1 1c0 1.25.2 2.45.57 3.57a1 1 0 0 1-.25 1z"/></svg>
      (41) 3000-0000
    </span>
  </footer>

  <svg class="edge-bands" viewBox="0 0 820 60" preserveAspectRatio="none">
    <polygon points="0,14 520,14 496,60 0,60" fill="var(--brand-navy)"/>
    <polygon points="536,28 820,28 820,60 520,60" fill="var(--brand-red)"/>
  </svg>
</main>
</body>
</html>
```